Bewerbungs-Template
Zielgruppe
Ich bin einen Einzelperson und möchte meine Bewerbungsunterlagen überarbeiten. Meine Zielgruppe ist ein potentieller Arbeitgeber welcher überzeugen möchte.
Aufgabenstellung
Das Design sollte professionell und übersichtlich aussehen und ein bisschen einzigartig sein. Es sollte nicht nur ein Deckblatt sein, wichtig ist für mich vor allem die CV-Gestaltung. Es muss kein Word-Format sein, kann mit den gängigen Office oder Photoprogrammen erstellt werden. In meinem Kopf schwirrt eine schlichte Idee mit einem Bordeaux-Roten Highlight herum, vlt. hat jemand eine Gute Idee :)
Ich bedanke mich bereits im Voraus für alle Ideen.

```html
<!DOCTYPE html>
<html lang="de">
<head>
<meta charset="utf-8">
<title>Bewerbungsmappe Heike Brandt</title>
<link rel="stylesheet" href="https://fonts.googleapis.com/css2?family=Inter:wght@700;800&family=Jost:wght@400;500&display=swap">
<style>
  :root{
    --black:#1c1a1f;
    --graphite:#3a393b;
    --fog:#e6e6e6;
    --white:#ffffff;
    --lemon:#fcf8cc;
    --sand:#ebe6b8;
    --signal:#ffe600;
    --ink:#1c1a1f;
  }
  *{margin:0;padding:0;box-sizing:border-box}
  html,body{width:1200px;height:914px;overflow:hidden;background:var(--white)}
  body{position:relative;font-family:"Jost",sans-serif;color:var(--ink)}
  .page{position:absolute;width:526px;height:372px;background:var(--white);overflow:hidden;box-shadow:0 6px 16px rgba(0,0,0,.35)}
  .page--cover{left:53px;top:59px}
  .page--cv{left:628px;top:59px}
  .page--letter{left:53px;top:461px}
  .page--attachments{left:628px;top:461px}
  .band{position:absolute;top:0;height:100%}
  .b-black{background:var(--black)}
  .b-graphite{background:var(--graphite)}
  .b-fog{background:var(--fog)}
  .b-lemon{background:var(--lemon)}
  .b-sand{background:var(--sand)}
  .b-signal{background:var(--signal)}
  .title-clip{position:absolute;overflow:hidden;height:30px}
  .title{position:absolute;top:0;white-space:nowrap;font-family:"Inter",sans-serif;font-weight:800;font-size:18px;letter-spacing:8.3px;line-height:30px}
  .on-dark{color:var(--white)}
  .on-light{color:var(--ink)}
  .kicker{position:absolute;font-family:"Inter",sans-serif;font-weight:700;font-size:5.2px;letter-spacing:3.1px;white-space:nowrap}
  .cover-name{left:154px;top:69px;color:var(--white)}
  .cover-name .bracket{color:var(--signal)}
  .portrait{position:absolute;left:268px;top:111px;width:93px;height:93px;background:linear-gradient(135deg,#8a8a88,#d2d1cd 55%,#6e6d6b)}
  .subtitle{position:absolute;top:333px;left:250px;font-family:"Inter",sans-serif;font-weight:700;font-size:5.3px;letter-spacing:3.3px;white-space:nowrap}
  .subtitle .on-dark{color:var(--white)}
  .section-head{position:absolute;font-family:"Inter",sans-serif;font-weight:700;font-size:5.2px;letter-spacing:3.2px;white-space:nowrap;color:var(--ink)}
  .facts{position:absolute;left:0;top:134px;width:200px}
  .fact{display:flex;height:9.45px;align-items:center}
  .fact-label{width:71px;text-align:right;font-size:4.3px;color:var(--white);padding-right:0}
  .fact-value{margin-left:7px;font-size:6px;color:var(--ink)}
  .entry{position:absolute;font-size:6px;line-height:9.3px;white-space:nowrap;color:var(--ink)}
  .period{position:absolute;left:287px;font-size:4.6px;font-weight:500;color:var(--white);white-space:nowrap}
  .letter-body{position:absolute;left:148px;top:49px;width:360px;font-size:5.8px;line-height:11.3px;color:var(--ink)}
  .letter-body p{margin-bottom:11.3px}
  .letter-body .close{margin-top:22px;margin-bottom:34px}
  .highlight{position:absolute;top:0;left:345px;width:65px;height:100%;background:var(--lemon);mix-blend-mode:multiply}
</style>
</head>
<body>

<section class="page page--cover">
  <div class="band b-fog" style="left:17px;width:12px"></div>
  <div class="band b-sand" style="left:29px;width:36px"></div>
  <div class="band b-fog" style="left:65px;width:67px"></div>
  <div class="band b-signal" style="left:132px;width:2px"></div>
  <div class="band b-graphite" style="left:134px;width:16px"></div>
  <div class="band b-black" style="left:150px;width:165px"></div>

  <div class="kicker cover-name"><span class="bracket">[</span>HEIKE BRANDT<span class="bracket">]</span></div>
  <div class="portrait" role="img" aria-label="Bewerbungsfoto der Bewerberin in Schwarzweiß"></div>

  <div class="title-clip" style="left:150px;width:165px;top:290px"><span class="title on-dark" style="left:62px">BEWERBUNG</span></div>
  <div class="title-clip" style="left:315px;width:211px;top:290px"><span class="title on-light" style="left:-103px">BEWERBUNG</span></div>

  <div class="subtitle"><span class="on-dark">BEWERBUNG </span><span>ALS STELLENBESCHREIBUNG</span></div>
</section>

<section class="page page--cv">
  <div class="band b-black" style="left:0;width:15px"></div>
  <div class="band b-signal" style="left:15px;width:2px"></div>
  <div class="band b-graphite" style="left:17px;width:58px"></div>
  <div class="band b-fog" style="left:75px;width:75px"></div>
  <div class="band b-black" style="left:278px;width:59px"></div>
  <div class="band b-graphite" style="left:337px;width:15px"></div>
  <div class="band b-fog" style="left:352px;width:119px"></div>
  <div class="band b-lemon" style="left:484px;width:27px"></div>

  <div class="title-clip" style="left:0;width:278px;top:16px"><span class="title on-light" style="left:157px">LEBENSLAUF</span></div>
  <div class="title-clip" style="left:278px;width:248px;top:16px"><span class="title on-dark" style="left:-121px">LEBENSLAUF</span></div>

  <div class="section-head" style="left:78px;top:116px">PERSÖNLICHE ANGABEN</div>
  <div class="facts">
    <div class="fact"><span class="fact-label">Name</span><span class="fact-value">Heike Brandt</span></div>
    <div class="fact"><span class="fact-label">Anschrift</span><span class="fact-value">Straßenname 12</span></div>
    <div class="fact"><span class="fact-label">Telefon</span><span class="fact-value">0123 012 345 67</span></div>
    <div class="fact"><span class="fact-label">E-Mail</span><span class="fact-value">ihre-email@beispielpost.de</span></div>
    <div class="fact"><span class="fact-label">Geburtsdatum</span><span class="fact-value">01. Januar 1997</span></div>
    <div class="fact"><span class="fact-label">Geburtsort</span><span class="fact-value">Stadtname</span></div>
    <div class="fact"><span class="fact-label">Staatsangehörigkeit</span><span class="fact-value">deutsch</span></div>
    <div class="fact"><span class="fact-label">Familienstand</span><span class="fact-value">ledig</span></div>
  </div>

  <div class="section-head" style="left:155px;top:248px">KENNTNISSE</div>
  <div class="entry" style="left:155px;top:264px">Englisch in Wort und Schrift<br>Französisch (3 Jahre)</div>
  <div class="section-head" style="left:155px;top:313px">SONSTIGES</div>
  <div class="entry" style="left:155px;top:330px">Besitz des Führerscheins Klasse B</div>

  <div class="section-head" style="left:354px;top:79px">SCHULBILDUNG</div>
  <div class="period" style="top:98px">09/2013 - 07/2016</div>
  <div class="entry" style="left:354px;top:96px">Angaben zur Schulbildung<br>Gymnasium Stadtname<br>Abitur</div>
  <div class="period" style="top:145px">09/2007 - 07/2013</div>
  <div class="entry" style="left:354px;top:143px">Realschule Stadtname<br>Mittlere Reife</div>
  <div class="section-head" style="left:354px;top:182px">BERUFSERFAHRUNG</div>
  <div class="period" style="top:201px">09/2015 - 07/2016</div>
  <div class="entry" style="left:354px;top:199px">Hier können Sie ihre<br>Berufserfahrung eingeben</div>
  <div class="section-head" style="left:354px;top:266px">HOBBYS</div>
  <div class="entry" style="left:354px;top:282px">lesen, zeichnen, Mode &amp; Beauty,<br>Fremdsprachen</div>
</section>

<section class="page page--letter">
  <div class="band b-black" style="left:0;width:17px"></div>
  <div class="band b-graphite" style="left:17px;width:58px"></div>
  <div class="band b-fog" style="left:75px;width:63px"></div>
  <div class="band b-signal" style="left:138px;width:2px"></div>

  <div class="title-clip" style="left:0;width:75px;top:16px"><span class="title on-dark" style="left:43px">ANSCHREIBEN</span></div>
  <div class="title-clip" style="left:75px;width:451px;top:16px"><span class="title on-light" style="left:-32px">ANSCHREIBEN</span></div>

  <div class="letter-body">
    <p>Sehr geehrte Damen und Herren,</p>
    <p>lorem ipsum dolor sit amet, consectetuer adipiscing elit. Aenean commodo ligula eget dolor.<br>Aenean massa. Cum sociis natoque penatibus et magnis dis parturient montes, nascetur ridiculus mus. Donec quam felis, ultricies nec, pellentesque eu, pretium quis, sem. Nulla consequat massa quis enim. Donec pede justo, fringilla vel, aliquet nec, vulputate eget, arcu. In enim justo,<br>rhoncus ut, imperdiet a, venenatis vitae, justo. Nullam dictum felis eu pede mollis pretium.</p>
    <p>Integer tincidunt. Cras dapibus. Vivamus elementum semper nisi. Aenean vulputate eleifend tellus. Aenean leo ligula, porttitor eu, consequat vitae, eleifend ac, enim. Aliquam lorem ante, dapibus in, viverra quis, feugiat a, tellus. Phasellus viverra nulla ut metus varius laoreet. Quisque rutrum. Aenean imperdiet. Etiam ultricies nisi vel augue. Curabitur ullamcorper ultricies nisi.</p>
    <p>Nam eget dui. Etiam rhoncus. Maecenas tempus, tellus eget condimentum rhoncus, sem quam semper libero, sit amet adipiscing sem neque sed ipsum. Nam quam nunc, blandit vel, luctus pulvinar, hendrerit id, lorem. Maecenas nec odio et ante tincidunt tempus. Donec vitae sapien ut libero venenatis faucibus. Nullam quis ante. Etiam sit amet orci eget eros faucibus tincidunt. Duis leo.<br>Sed fringilla mauris sit amet nibh. Donec sodales sagittis magna. Sed consequat, leo eget<br>bibendum sodales, augue velit cursus nunc.</p>
    <p class="close">Mit freundlichen Grüßen</p>
    <p>Heike Brandt</p>
  </div>
  <div class="highlight"></div>
</section>

<section class="page page--attachments">
  <div class="band b-black" style="left:142px;width:15px"></div>
  <div class="band b-signal" style="left:157px;width:2px"></div>
  <div class="band b-graphite" style="left:159px;width:58px"></div>
  <div class="band b-fog" style="left:217px;width:63px"></div>
  <div class="band b-lemon" style="left:352px;width:112px"></div>

  <div class="title-clip" style="left:142px;width:75px;top:16px"><span class="title on-dark" style="left:43px">ANLAGEN</span></div>
  <div class="title-clip" style="left:217px;width:309px;top:16px"><span class="title on-light" style="left:-32px">ANLAGEN</span></div>
</section>

</body>
</html>
```